Brisk Orchard LLC- AED's

To promote the sale of AED's (Automated External Defibrillators) as well as supplies such as Batteries, Pads, Cases, and Cabinets (indoor and outdoor)
Other products for sale, First Aid kits, Bleeding control kits, CPR masks, Tourniquets.
I would like to have all of the front side to be about AED's and supplies, the back to focus on the other products forsale, contact info, and training offerings.
I have attached my existing copy of my current training flyer and would like to try to match that format the best that you can.

tri fold format please. Thank you all

```html
<!DOCTYPE html>
<html lang="en">
<head>
<meta charset="utf-8">
<title>Brisk Orchard LLC – AED Tri-fold Brochure</title>
<link href="https://fonts.googleapis.com/css2?family=Oswald:wght@700&family=Rubik:wght@500;700&family=Fira+Sans:wght@400;500;600&family=Poppins:wght@300&display=swap" rel="stylesheet">
<style>
  :root{
    --red:#c8202a;
    --ink:#1f1f1f;
    --text:#2b2b2b;
    --panel-grey:#e8e8e8;
    --swoosh:#7c7c7c;
    --page:#dcdcdc;
    --white:#ffffff;
  }
  *{box-sizing:border-box;margin:0;padding:0}
  html,body{width:1200px;height:1200px;overflow:hidden}
  body{background:var(--page);position:relative;font-family:"Poppins",sans-serif;color:var(--text)}
  .sheet{position:absolute;left:263px;width:674px;height:520px;background:var(--white);overflow:hidden;box-shadow:0 4px 14px rgba(0,0,0,.25)}
  .sheet--outside{top:64px}
  .sheet--inside{top:624px}
  .sheet__bg,.sheet__overlay{position:absolute;left:0;top:0;width:674px;height:520px}
  .abs{position:absolute}
  .photo{position:absolute}
  .body-copy{font-family:"Poppins",sans-serif;font-weight:300;font-size:6.7px;line-height:9.6px;text-align:justify;color:var(--text)}
  .body-copy p+p{margin-top:9px}
  .section-title{font-family:"Rubik",sans-serif;font-weight:700;font-size:11.5px;color:var(--red);text-transform:uppercase}
  .sub-title{font-family:"Rubik",sans-serif;font-weight:500;font-size:11.5px}
  .logo-badge{position:absolute;border-radius:50%;background:var(--white);display:flex;align-items:center;justify-content:center;text-align:center;font-family:"Fira Sans",sans-serif;font-weight:600;color:var(--ink);line-height:1.1}
  .intro-lead{font-family:"Fira Sans",sans-serif;font-weight:500;font-size:9.2px;line-height:11.8px;text-align:center;color:var(--ink)}
  .contact{position:absolute;left:225px;width:225px;top:360px;text-align:center;color:var(--white);font-family:"Fira Sans",sans-serif;font-size:7.6px;line-height:10px}
  .contact__title{font-family:"Rubik",sans-serif;font-weight:700;font-size:14px;letter-spacing:.3px;margin-bottom:6px}
  .contact__icon{display:block;margin:0 auto 3px;width:13px;height:13px}
  .contact__item{margin-bottom:7px}
  .hero-title{position:absolute;left:450px;width:224px;top:278px;text-align:center;font-family:"Oswald",sans-serif;font-weight:700;font-size:25px;line-height:31px;text-transform:uppercase;letter-spacing:.2px}
  .hero-title .red{color:var(--red)}
  .hero-title .dark{color:var(--ink)}
  .hero-copy{position:absolute;left:460px;width:204px;top:380px;text-align:center;font-family:"Fira Sans",sans-serif;font-weight:400;font-size:9.8px;line-height:13.4px;color:var(--ink)}
  .site-pill{position:absolute;left:496px;top:487px;width:133px;height:18px;border-radius:9px;background:var(--red);color:var(--white);font-family:"Fira Sans",sans-serif;font-weight:600;font-size:9px;letter-spacing:1px;line-height:18px;text-align:center}
  .red-copy{color:var(--white)}
  .red-copy .body-copy{color:var(--white);font-size:6.4px;line-height:9px;letter-spacing:-.1px}
  .red-copy .body-copy p+p{margin-top:5px}
  .tick-list{list-style:none;margin-top:2px}
  .tick-list li{position:relative;padding-left:9px;font-family:"Poppins",sans-serif;font-weight:300;font-size:6.3px;line-height:8.2px;letter-spacing:-.1px;color:var(--white);margin-bottom:1px}
  .tick-list li svg{position:absolute;left:0;top:1.2px;width:6px;height:6px}
</style>
</head>
<body>

<section class="sheet sheet--outside" aria-label="Brochure outside spread">
  <svg class="sheet__bg" viewBox="0 0 674 520" aria-hidden="true">
    <rect x="225" y="0" width="225" height="520" fill="var(--red)"/>
    <path d="M225 0 H450 V232 Q340 190 225 172 Z" fill="var(--panel-grey)"/>
    <path d="M450 0 H674 V188 Q560 212 450 232 Z" fill="var(--red)"/>
  </svg>

  <div class="photo" style="left:0;top:0;width:225px;height:195px;background:linear-gradient(135deg,#8a6a4a 0%,#e0892c 40%,#3b3b3b 75%,#b8a58c 100%)" role="img" aria-label="Photo of a rescuer carrying an orange AED unit in a shoulder case"></div>
  <div class="photo" style="left:241px;top:146px;width:196px;height:98px;border-radius:6px;background:linear-gradient(135deg,#f3f3f3 0%,#f2d440 40%,#5a80b8 75%,#e9e9e9 100%)" role="img" aria-label="Assortment of AED supplies: electrode pads, batteries and replacement packs"></div>
  <div class="photo" style="left:461px;top:160px;width:202px;height:106px;border-radius:6px;background:linear-gradient(120deg,#f2c230 0%,#f07a1c 35%,#9ac53b 55%,#2e3a58 75%,#d8202b 100%)" role="img" aria-label="Group of AED units from several makers in yellow, orange, green, navy and red"></div>

  <svg class="sheet__overlay" viewBox="0 0 674 520" aria-hidden="true">
    <path d="M0 188 Q110 174 225 170 L225 260 L0 260 Z" fill="var(--white)"/>
    <path d="M0 188 Q110 174 225 170 Q340 190 450 232 Q560 212 674 188" fill="none" stroke="var(--swoosh)" stroke-width="5"/>
  </svg>

  <h2 class="section-title abs" style="left:18px;top:201px">History of AEDs</h2>
  <div class="body-copy abs" style="left:18px;top:217px;width:190px">
    <p>Defibrillation was first demonstrated in 1899 by Marchand &amp; Rossetti, two physiologists from Lakeside University, Switzerland. They discovered that small electric shocks could induce ventricular fibrillation. The first use of a defibrillator on a human was in 1947 by Walter Hale, professor of surgery at Northshore Medical College. Hale first used the technique of defibrillation successfully on a 14 year old boy who was being operated on for a congenital chest defect. In the 1960s, portable defibrillators were introduced for use in ambulances. Today, defibrillators are the only proven way to resuscitate a person who has had a cardiac arrest and is still in persistent ventricular fibrillation or ventricular tachycardia at the arrival of rescuers.</p>
    <p>Sudden cardiac arrest is a major public health problem and affects an estimated 500,000 people every year. Sudden cardiac arrest can strike anyone, so it is extremely important to be prepared to respond quickly to sudden cardiac arrest. Having an accessible Automated External Defibrillator (AED) used to quickly deliver a life-saving shock often means the difference between life and death. When a victim experiences sudden cardiac arrest, with a shockable rhythm, every minute counts; every minute a victim goes without defibrillation, the chances for survival decrease by 7%-10%. But having an AED installed at your location can allow on-site trained responders, or nearby emergency responders, deliver potentially life-saving defibrillation therapy quickly and effectively.</p>
  </div>

  <p class="intro-lead abs" style="left:236px;top:30px;width:203px">An AED, or automated external defibrillator, is used to help those experiencing sudden cardiac arrest. It's a sophisticated, yet easy-to-use, medical device that can analyze the heart's rhythm and if necessary, deliver an electrical shock, or defibrillation, to help the heart re-establish an effective rhythm</p>

  <div class="logo-badge" style="left:291px;top:259px;width:92px;height:92px;font-size:12px">Brisk<br>Orchard</div>

  <div class="contact">
    <h2 class="contact__title">CONTACT US</h2>
    <div class="contact__item">
      <svg class="contact__icon" viewBox="0 0 14 14"><circle cx="7" cy="7" r="7" fill="#fff"/><path d="M7 3.2a2.5 2.5 0 0 0-2.5 2.5C4.5 7.6 7 10.8 7 10.8s2.5-3.2 2.5-5.1A2.5 2.5 0 0 0 7 3.2z" fill="var(--red)"/><circle cx="7" cy="5.7" r=".9" fill="#fff"/></svg>
      418 Birchwood Ln, Maple Ridge,<br>MI, United States, 49000
    </div>
    <div class="contact__item">
      <svg class="contact__icon" viewBox="0 0 14 14"><circle cx="7" cy="7" r="7" fill="#fff"/><path d="M4.6 3.6l1.3-.3.8 1.9-.9.7c.4.9 1.1 1.6 2 2l.7-.9 1.9.8-.3 1.3c-3 .3-5.8-2.5-5.5-5.5z" fill="var(--red)"/></svg>
      (555) 014-2290
    </div>
    <div class="contact__item">
      <svg class="contact__icon" viewBox="0 0 14 14"><circle cx="7" cy="7" r="7" fill="#fff"/><rect x="3.6" y="4.6" width="6.8" height="4.8" rx=".5" fill="var(--red)"/><path d="M3.8 4.9 7 7.3l3.2-2.4" fill="none" stroke="#fff" stroke-width=".7"/></svg>
      info@briskorchard.org
    </div>
    <div class="contact__item">
      <svg class="contact__icon" viewBox="0 0 14 14"><circle cx="7" cy="7" r="7" fill="#fff"/><circle cx="7" cy="7" r="3.6" fill="none" stroke="var(--red)" stroke-width=".9"/><path d="M3.4 7h7.2M7 3.4c-1.6 2-1.6 5.2 0 7.2M7 3.4c1.6 2 1.6 5.2 0 7.2" fill="none" stroke="var(--red)" stroke-width=".7"/></svg>
      www.briskorchard.org
    </div>
  </div>

  <div class="logo-badge" style="left:508px;top:23px;width:110px;height:110px;font-size:14px">Brisk<br>Orchard</div>
  <h1 class="hero-title"><span class="red">Health and</span><br><span class="dark">Safety Education</span><br><span class="red">in Michigan</span></h1>
  <p class="hero-copy">At Brisk Orchard, we've been providing effective, easy and engaging lifesaving solutions for years to our communities in Michigan. Read on to learn how we offer support to those who need it and how we're improving people's well-being.</p>
  <div class="site-pill">www.briskorchard.org</div>
</section>

<section class="sheet sheet--inside" aria-label="Brochure inside spread">
  <svg class="sheet__bg" viewBox="0 0 674 520" aria-hidden="true">
    <rect x="225" y="0" width="225" height="520" fill="var(--red)"/>
  </svg>

  <div class="photo" style="left:0;top:0;width:225px;height:190px;background:linear-gradient(135deg,#3a3a3a 0%,#b89a80 40%,#ece3cf 65%,#6b6b6b 100%)" role="img" aria-label="Photo of hands performing chest compressions on a CPR training manikin with AED pads"></div>
  <div class="photo" style="left:225px;top:0;width:225px;height:190px;background:linear-gradient(135deg,#ffffff 0%,#e6e6e6 45%,#d23a30 60%,#f1f1f1 100%)" role="img" aria-label="Photo of an open white AED unit with numbered pad placement steps"></div>
  <div class="photo" style="left:450px;top:0;width:224px;height:215px;background:linear-gradient(135deg,#5a5d66 0%,#b9dd3a 40%,#a3c82c 65%,#8a8e96 100%)" role="img" aria-label="Photo of a lime green AED unit resting on grey carpet"></div>

  <svg class="sheet__overlay" viewBox="0 0 674 520" aria-hidden="true">
    <path d="M0 182 Q120 168 225 176 L225 260 L0 260 Z" fill="var(--white)"/>
    <path d="M225 176 Q340 172 450 232 L450 260 L225 260 Z" fill="var(--red)"/>
    <path d="M450 234 Q560 226 674 186 L674 260 L450 260 Z" fill="var(--white)"/>
    <path d="M0 180 Q120 166 225 174 Q340 176 450 232 Q560 226 674 184" fill="none" stroke="var(--swoosh)" stroke-width="5"/>
  </svg>

  <div class="body-copy abs" style="left:18px;top:196px;width:190px">
    <p>Compressions keep the oxygen carrying blood circulating to the vital organs and these organs send the correct electrical signals to the heart to beat in a life sustaining sequence. Secondly, when the heart goes into a rhythm that does not allow the chambers to contract in the right sequence to pass the blood through, the rapid use of an AED sends a shock to the heart to assist in resetting it to a rhythm that can again sustain life.</p>
    <p>Every. Second. COUNTS. Having quick access to an AED is crucial. We commonly hear in our classes that we have help around the corner so we can just start CPR and wait for an AED. Something everyone needs to think about is whether that help is really there? Commonly EMS and Rescue units are busy helping others. Your ambulance or rescue unit assigned to you could be coming from the other side of your city, or another township, or in extreme circumstances another county. For the average patient, an AED needs to be utilized within a 10-minute window. The patient on average loses a 10% chance of survival every minute that goes by without an AED placed in a cardiac arrest event. It is amazing how many minutes are lost just calling 911, having the emergency units get out the door, and the time it takes to drive to your location.</p>
    <p>The more people that are trained in CPR/AEDs and the more AED units there are installed within a community, the bigger the impact on public safety. Let's get these units in every business and public access point that we can.</p>
  </div>

  <div class="red-copy abs" style="left:243px;top:214px;width:192px">
    <h2 class="sub-title" style="color:var(--white);margin-bottom:3px">Who can use an AED?</h2>
    <div class="body-copy">
      <p>Because of the need for an instant on-site response to a sudden cardiac arrest, AED technology &amp; laws regarding their use have been purposely developed so that virtually anyone, even a child, can put them to use in an emergency situation. While there are very sophisticated forms of the AED which are typically deployed by emergency medical personnel with advanced knowledge &amp; training in treating heart attacks, there are also very simple versions for use by any bystander. Thus it is most important that public awareness be aroused as to the existence of these machines, the circumstances in which they should be used, &amp; the need to have AEDs accessible in every possible setting.</p>
      <p>The significance of AEDs in guarding public health has led to the adoption of laws by various states of the U.S. This began officially in 1997 with Florida, and as of 2010 all 50 states have since enacted laws &amp;/or regulations regarding defibrillator use. All this is in the hope of increasing the chances of survival for an SCA victim.</p>
    </div>
    <h3 style="font-family:'Rubik',sans-serif;font-weight:500;font-size:7.4px;margin-top:5px">States are working to:</h3>
    <ul class="tick-list">
      <li><svg viewBox="0 0 6 6"><circle cx="3" cy="3" r="3" fill="#fff"/><path d="M1.6 3.1l1 .9 1.8-1.9" fill="none" stroke="var(--red)" stroke-width=".8"/></svg>Make AEDs more available,</li>
      <li><svg viewBox="0 0 6 6"><circle cx="3" cy="3" r="3" fill="#fff"/><path d="M1.6 3.1l1 .9 1.8-1.9" fill="none" stroke="var(--red)" stroke-width=".8"/></svg>Normalize public AED use,</li>
      <li><svg viewBox="0 0 6 6"><circle cx="3" cy="3" r="3" fill="#fff"/><path d="M1.6 3.1l1 .9 1.8-1.9" fill="none" stroke="var(--red)" stroke-width=".8"/></svg>Encourage AED training,</li>
      <li><svg viewBox="0 0 6 6"><circle cx="3" cy="3" r="3" fill="#fff"/><path d="M1.6 3.1l1 .9 1.8-1.9" fill="none" stroke="var(--red)" stroke-width=".8"/></svg>Require that maintenance and testing meet manufacturers' standards,</li>
      <li><svg viewBox="0 0 6 6"><circle cx="3" cy="3" r="3" fill="#fff"/><path d="M1.6 3.1l1 .9 1.8-1.9" fill="none" stroke="var(--red)" stroke-width=".8"/></svg>Sreate a registry of defibrillator locations,</li>
      <li><svg viewBox="0 0 6 6"><circle cx="3" cy="3" r="3" fill="#fff"/><path d="M1.6 3.1l1 .9 1.8-1.9" fill="none" stroke="var(--red)" stroke-width=".8"/></svg>Establish a "Good Samaritan" exemption from liability,</li>
      <li><svg viewBox="0 0 6 6"><circle cx="3" cy="3" r="3" fill="#fff"/><path d="M1.6 3.1l1 .9 1.8-1.9" fill="none" stroke="var(--red)" stroke-width=".8"/></svg>Determine more detailed requirements for AED certification and registration.</li>
    </ul>
  </div>

  <div class="abs" style="left:468px;top:248px;width:190px">
    <h2 class="sub-title" style="color:var(--ink);margin-bottom:5px">When is an AED needed?</h2>
    <div class="body-copy">
      <p>AEDs are used to revive someone from sudden cardiac arrest. This usually occurs when a disruption in the heart's electrical activity causes a dangerously fast heartbeat (ventricular tachycardia) or a fast &amp; irregular heartbeat (ventricular fibrillation). Either of these irregular heart rhythms keeps the heart from pumping effectively and can cause it to stop.</p>
      <p>When this happens, the brain and other vital organs don't get the blood and oxygen they need. This requires treatment within minutes to prevent death. The sooner the heart's rhythm is restored, the greater the chance there won't be permanent damage to the brain and other organs.</p>
      <p>If an AED is near someone having ventricular fibrillation or ventricular tachycardia, a bystander in a public place or a family member can use it to jolt the heart back to a regular rhythm. Using the AED could possibly save a life. Cardiopulmonary resuscitation (CPR) after cardiac arrest can keep blood flowing to the heart and brain for a time. But often only defibrillation can restore the heart's rhythm. Together these treatments can improve the chances of survival.</p>
    </div>
  </div>
</section>

</body>
</html>
```